Website Design for a High School

School Name: Bayt Qamarin Private Schools
sub-schools:
1-Bayt Qamarin Primary School
2-Bayt Qamarin High School for Girls
3-Bayt Qamarin High School for Boys
The design should be professional and serious and below is the details of the website.
Pages: (Home, About Us, Schools, Events, Students, Gallery, Lectures, Contact Us).
A-) Home Page:
1-Animated photos banner as main
2-Marquee for the last news.
3-Welcoming block of text
4-latest news at the body of the page.
5-Calender "on the side"
6-Number of visitors "on the side"
7-Search bar
8-options to choose a school
B-) School Page:
three schools listed as drop down menu when highlighted over the Schools button in the menu
*Each school page should contain:
1-Student login area
2-Animation photos header
3-Specific news and projects
C-) Student Login page:
have a Report Card
D-) Gallery Page
have a collection of photos.
E-)Contact Page
phone numbers
emails
feedback form
F-)Other mentioned pages
with normal text and photos page look as similar to the Home page.
Required color: Purple as main and include the logo colors
Logo: is attached.
Button link to change language to Arabic.

```html
<!DOCTYPE html>
<html lang="en">
<head>
<meta charset="utf-8">
<title>Bayt Qamarin Private Schools</title>
<link rel="stylesheet" href="https://fonts.googleapis.com/css2?family=Roboto+Condensed:wght@400;700&family=Open+Sans:wght@400;600&display=swap">
<style>
:root{
  --purple:#6a3f9e;
  --purple-dark:#55307f;
  --purple-soft:#8d66b5;
  --ink:#333;
  --muted:#777;
  --line:#ddd;
  --panel:#f2f2f2;
  --white:#fff;
  --yellow:#f7d54a;
  --yellow-dark:#ebb92e;
  --head:"Roboto Condensed",Arial,sans-serif;
  --body:"Open Sans",Arial,sans-serif;
}
*{box-sizing:border-box;margin:0;padding:0}
html,body{width:1200px;height:2359px;overflow:hidden;background:var(--white);font-family:var(--body);color:var(--ink)}
.page{position:relative;width:1200px;height:2359px}
section,header,footer{position:relative;width:1200px}
.abs{position:absolute}

/* header */
.site-header{height:180px;background:var(--white)}
.brand{position:absolute;left:28px;top:22px;width:200px;height:200px;border-radius:50%;background:var(--white);border:6px solid var(--purple);z-index:3;display:flex;align-items:center;justify-content:center;text-align:center;padding:24px;font-family:var(--head);font-weight:700;font-size:22px;line-height:1.2;color:var(--purple)}
.visitor-counter{left:530px;top:32px;display:flex;gap:8px}
.visitor-counter span{width:52px;height:56px;background:var(--purple);color:var(--white);font-family:var(--head);font-weight:700;font-size:38px;display:flex;align-items:center;justify-content:center;border-radius:3px}
.header-phone{left:900px;top:44px;display:flex;align-items:center;gap:8px;font-family:var(--head);font-size:26px;color:var(--ink)}
.search-btn{left:1118px;top:38px;width:44px;height:44px;border-radius:50%;background:var(--purple);display:flex;align-items:center;justify-content:center}
.main-nav{left:312px;top:115px;display:flex;gap:0;font-family:var(--head);font-size:18px}
.main-nav a{display:block;padding:0 19px;height:46px;line-height:46px;color:var(--purple-dark);text-decoration:none;text-transform:uppercase}
.main-nav a.active{background:var(--purple);color:var(--white);border:2px solid #bfa6dc}

.hero{height:541px;background:linear-gradient(100deg,#c23a3a 0%,#b23333 15%,#3f5a52 30%,#3a4f49 70%,#4b5e58 100%)}

/* welcome */
.welcome{height:309px;background:var(--white);padding:0 28px}
.section-title{font-family:var(--head);font-weight:700;font-size:27px;color:#222;text-transform:uppercase}
.section-title em{font-style:normal;color:var(--purple)}
.title-rule{height:2px;width:380px;background:var(--line);margin-top:10px}
.welcome .section-title{position:absolute;left:28px;top:40px}
.welcome p{position:absolute;left:28px;top:110px;width:1130px;font-size:16.5px;line-height:31px;color:#444}
.read-more-link{position:absolute;right:40px;top:252px;font-family:var(--head);font-size:16px;color:var(--purple-dark);text-transform:uppercase}

/* projects */
.projects{height:555px;background:var(--panel)}
.projects .section-title{position:absolute;left:28px;top:38px}
.project-card{position:absolute;top:112px;width:357px;height:394px;background:var(--white);box-shadow:0 1px 6px rgba(0,0,0,.15);text-align:center}
.project-card h3{font-family:var(--head);font-weight:400;font-size:23px;color:var(--purple-dark);text-transform:uppercase;height:72px;line-height:72px}
.project-photo{height:175px;margin:0 0}
.project-card p{font-size:14.5px;line-height:22px;color:var(--muted);padding:28px 50px 0;height:80px}
.btn{display:inline-block;background:var(--purple);color:var(--white);font-family:var(--head);font-weight:700;font-size:14px;padding:0 16px;height:38px;line-height:38px;text-transform:uppercase;margin-top:26px}

/* news + calendar */
.news{height:415px;background:var(--white)}
.news .section-title{position:absolute;top:36px}
.news-item{position:absolute;top:108px;width:357px}
.news-photo{height:168px}
.news-meta{display:flex;gap:14px;margin-top:14px}
.date-badge{width:68px;height:74px;border:2px solid var(--purple);text-align:center;font-family:var(--head)}
.date-badge b{display:block;font-size:24px;line-height:36px;border-bottom:2px solid var(--purple)}
.date-badge span{display:block;font-size:13px;line-height:17px;color:#555}
.news-meta p{font-size:16px;line-height:27px;color:var(--purple-dark);padding-top:14px}
.calendar{position:absolute;left:811px;top:108px;width:345px;border:1px solid var(--line);padding:2px}
.cal-head{background:var(--purple);color:var(--white);height:34px;display:flex;align-items:center;justify-content:space-between;padding:0 10px;font-family:var(--head);font-size:17px}
.calendar table{width:100%;border-collapse:separate;border-spacing:2px;font-size:15px;text-align:center}
.calendar th{background:#ccc;height:28px;font-weight:600;font-size:14px}
.calendar td{background:#eee;height:30px}
.calendar td.blank{background:#eee}
.calendar td.on{background:var(--purple);color:var(--white)}
.calendar td.today{background:#f8ea4f}

/* contact */
.contact{height:280px;background:var(--purple-soft);color:var(--white)}
.contact h4{position:absolute;top:36px;font-family:var(--head);font-weight:700;font-size:20px;text-transform:uppercase}
.field{position:absolute;background:var(--white);border-radius:8px;color:#666;font-size:15px;padding:14px 20px}
.submit-btn{position:absolute;left:666px;top:140px;width:120px;height:110px;border-radius:6px;background:linear-gradient(135deg,var(--yellow) 50%,var(--yellow-dark) 50%);color:var(--purple-dark);font-family:var(--head);font-weight:700;font-size:19px;display:flex;align-items:center;justify-content:center}
.visit-line{position:absolute;left:829px;display:flex;gap:14px;font-size:15px;line-height:22px;font-weight:600}

/* bottom */
.bottom-bar{height:79px;background:var(--white)}
.copyright{position:absolute;left:28px;top:32px;font-size:15px;color:#555}
.copyright b{font-weight:400;color:var(--purple)}
.social{position:absolute;left:910px;top:20px;display:flex;gap:13px}
.social span{width:40px;height:40px;border-radius:50%;border:2px solid #ccc}
.social span.first{background:var(--purple);border-color:var(--purple)}
</style>
</head>
<body>
<div class="page">

<header class="site-header">
  <div class="brand">Bayt Qamarin Private Schools</div>
  <div class="abs visitor-counter"><span>1</span><span>0</span><span>0</span><span>0</span><span>0</span></div>
  <div class="abs header-phone">
    <svg width="22" height="26" viewBox="0 0 22 26"><path d="M5 2l4 6-3 3c1 4 4 7 8 9l3-3 5 4-3 4C9 24 1 14 2 5z" fill="none" stroke="#666" stroke-width="2"/></svg>
    123 456 7890
  </div>
  <div class="abs search-btn"><svg width="20" height="20" viewBox="0 0 20 20"><circle cx="8" cy="8" r="6" fill="none" stroke="#fff" stroke-width="2.5"/><path d="M12.5 12.5l6 6" stroke="#fff" stroke-width="2.5"/></svg></div>
  <nav class="abs main-nav">
    <a class="active">Home</a><a>About Us</a><a>Schools</a><a>Students</a><a>Events</a><a>Gallery</a><a>Lectures</a><a>Contact Us</a>
  </nav>
</header>

<section class="hero" role="img" aria-label="Banner photo of an excited schoolboy with glasses pointing upward in front of a chalkboard covered in maths and chemistry sketches"></section>

<section class="welcome">
  <h2 class="section-title">Welcome to <em>Bayt Qamarin Private Schools</em></h2>
  <div class="abs title-rule" style="left:28px;top:84px;width:1144px"></div>
  <p>Lorem ipsum dolor sit amet, consectetur adipiscing elit. Nulla convallis, nulla eget vulputate rutrum, tellus elit cursus erat, efficitur tristi que ex purus et lacus. Interdum et males uada fames ac ante ipsum primis in fauc ibus. Praesent non volutpat nibh, id condim entum nibh. Proin quis nulla quam. Mauris vitae pretium est. Aenean ultricies efficitur eros. In ullamcorper ut orci id posuere. Cras in pellent esque felis, et euismod mauris. Nullam a risus sit amet leo malesuada rhoncus.</p>
  <span class="read-more-link">Read more &nbsp;›</span>
</section>

<section class="projects">
  <h2 class="section-title">Our <em>Projects</em></h2>
  <div class="abs title-rule" style="left:28px;top:84px;width:180px"></div>
  <article class="project-card" style="left:28px">
    <h3>Primary School</h3>
    <div class="project-photo" role="img" aria-label="Photo of young pupils working together at a desk with their teacher" style="background:linear-gradient(90deg,#8a6a52,#d8b48e,#c9a889)"></div>
    <p>Lorem ipsum dolor sit amet, consect etur adipiscing elit cursus erat.</p>
    <span class="btn">Read more</span>
  </article>
  <article class="project-card" style="left:417px">
    <h3>High School for Girls</h3>
    <div class="project-photo" role="img" aria-label="Photo of a smiling schoolgirl at a desk surrounded by sketched school doodles" style="background:linear-gradient(90deg,#e6e6e6,#d9c7a8,#ececec)"></div>
    <p>Lorem ipsum dolor sit amet, consect etur adipiscing elit cursus erat.</p>
    <span class="btn">Read more</span>
  </article>
  <article class="project-card" style="left:806px">
    <h3>High School for Boys</h3>
    <div class="project-photo" role="img" aria-label="Photo of a schoolboy in glasses lying on the floor reading a book" style="background:linear-gradient(90deg,#f1f1f1,#c8cfdc,#ededed)"></div>
    <p>Lorem ipsum dolor sit amet, consect etur adipiscing elit cursus erat.</p>
    <span class="btn">Read more</span>
  </article>
</section>

<section class="news">
  <h2 class="section-title" style="left:28px">Latest <em>News</em></h2>
  <div class="abs title-rule" style="left:28px;top:80px;width:155px"></div>
  <h2 class="section-title" style="left:811px"><em>Calender</em></h2>
  <div class="abs title-rule" style="left:811px;top:80px;width:165px"></div>

  <article class="news-item" style="left:28px">
    <div class="news-photo" role="img" aria-label="Photo of a teacher helping children at classroom computers" style="background:linear-gradient(90deg,#4a3326,#9a7356,#5c4434)"></div>
    <div class="news-meta">
      <div class="date-badge"><b>29</b><span>Feb<br>2015</span></div>
      <p>Lorem ipsum dolor sit amet cons etur adipiscing elit.</p>
    </div>
  </article>
  <article class="news-item" style="left:419px">
    <div class="news-photo" role="img" aria-label="Black and white photo of a cheering schoolboy in front of a chalkboard" style="background:linear-gradient(90deg,#2e2e2e,#8a8a8a,#3b3b3b)"></div>
    <div class="news-meta">
      <div class="date-badge"><b>29</b><span>Feb<br>2015</span></div>
      <p style="color:#555">Lorem ipsum dolor sit amet cons etur adipiscing elit.</p>
    </div>
  </article>

  <div class="calendar">
    <div class="cal-head"><span>‹</span><span>May 2015</span><span>›</span></div>
    <table>
      <tr><th>M</th><th>T</th><th>W</th><th>T</th><th>F</th><th>S</th><th>S</th></tr>
      <tr><td class="blank"></td><td class="blank"></td><td>1</td><td>2</td><td>3</td><td class="today">4</td><td>5</td></tr>
      <tr><td>6</td><td class="on">7</td><td>8</td><td>9</td><td>10</td><td>11</td><td class="on">12</td></tr>
      <tr><td>13</td><td>14</td><td>15</td><td>16</td><td>17</td><td>18</td><td>19</td></tr>
      <tr><td>20</td><td class="on">21</td><td class="on">22</td><td class="on">23</td><td>24</td><td>25</td><td>26</td></tr>
      <tr><td>27</td><td>28</td><td class="on">29</td><td>30</td><td>31</td><td class="blank"></td><td class="blank"></td></tr>
    </table>
  </div>
</section>

<section class="contact">
  <h4 style="left:28px">Contact Us</h4>
  <div class="field" style="left:28px;top:73px;width:370px;height:48px">Your Name:</div>
  <div class="field" style="left:417px;top:73px;width:369px;height:48px">Email:</div>
  <div class="field" style="left:28px;top:140px;width:620px;height:110px">Comments:</div>
  <div class="submit-btn">SUBMIT</div>

  <h4 style="left:829px">Visit to Qamarin</h4>
  <div class="visit-line" style="top:74px">
    <svg width="26" height="30" viewBox="0 0 26 30"><path d="M13 2v26M4 6h18l-3 4 3 4H4z" fill="none" stroke="#f7d54a" stroke-width="2.5"/></svg>
    <span>PO Box: 0000, Lorem ipsum dolor sit<br>consectetur Victoria, Australia 12345</span>
  </div>
  <div class="visit-line" style="top:152px">
    <svg width="26" height="26" viewBox="0 0 22 26"><path d="M5 2l4 6-3 3c1 4 4 7 8 9l3-3 5 4-3 4C9 24 1 14 2 5z" fill="none" stroke="#f7d54a" stroke-width="2.5"/></svg>
    <span>123 456 7890 &nbsp;/&nbsp; 012 345 6789</span>
  </div>
  <div class="visit-line" style="top:224px">
    <svg width="26" height="20" viewBox="0 0 26 20"><rect x="1" y="2" width="24" height="16" fill="none" stroke="#f7d54a" stroke-width="2.5"/><path d="M1 2l12 9 12-9" fill="none" stroke="#f7d54a" stroke-width="2.5"/></svg>
    <span>info@baytqamarin.edu</span>
  </div>
</section>

<footer class="bottom-bar">
  <p class="copyright">Copyright © 2015, <b>Bayt Qamarin Private Schools.</b> &nbsp;Privacy Policy | Terms of Use</p>
  <div class="social"><span class="first"></span><span></span><span></span><span></span><span></span></div>
</footer>

</div>
</body>
</html>
```